New website for tarnholm.se using wordpress

- Tarnholm is a consultant broker based in Sweden
- Current web page: tarnholm.se
- We want a new web page and we are aiming for simple and "clean"
- Two target groups:
1. Consultants/Consultant firms looking for assignments
2. Clients looking for consultants
- Colors + Logo attached

Requirements
Must have
• The new site should have separate pages the different sections. We have to be able to link to each page separately. NOT like the current web page where all the content is on one page.

```html
<!DOCTYPE html>
<html lang="sv">
<head>
<meta charset="utf-8">
<title>Tarnholm – Konsultmäkleri</title>
<link href="https://fonts.googleapis.com/css2?family=Quicksand:wght@500;600;700&family=Lato:wght@400;700&display=swap" rel="stylesheet">
<style>
:root{
  --purple:#5b2a9a;
  --purple-dark:#4a1f85;
  --purple-soft:#ece6f4;
  --ink:#1d1d1f;
  --text:#333;
  --grey:#5d6166;
  --line:#ddd;
  --footer:#0c0c0c;
  --white:#fff;
}
*{box-sizing:border-box;margin:0;padding:0}
html,body{width:1200px;height:4461px;overflow:hidden}
body{position:relative;font-family:'Lato',sans-serif;color:var(--text);background:var(--white)}
.abs{position:absolute}
.heading{font-family:'Quicksand',sans-serif;font-weight:700;color:var(--ink)}

/* header */
.site-header{position:absolute;left:0;top:0;width:1200px;height:118px;background:var(--white);z-index:3}
.brand-box{position:absolute;left:112px;top:0;width:201px;height:161px;background:var(--purple);z-index:4;display:flex;align-items:flex-end;justify-content:center;padding-bottom:22px}
.brand-name{font-family:'Quicksand',sans-serif;font-weight:700;font-size:34px;color:var(--white);letter-spacing:1px}
.main-nav a{position:absolute;top:52px;font-size:15px;color:#333;text-decoration:none;text-transform:uppercase}
.search-icon{position:absolute;left:1064px;top:50px}

/* hero */
.hero{position:absolute;left:0;top:118px;width:1200px;height:641px;
  background:linear-gradient(180deg,#6f8aa0 0%,#a9a7a0 30%,#d9a86a 50%,#7a6a5a 60%,#3a3e48 75%,#52565c 100%)}
.hero-title{position:absolute;left:0;width:1200px;top:130px;text-align:center;font-family:'Quicksand',sans-serif;font-weight:700;font-size:52px;line-height:69px;color:var(--white);letter-spacing:1px}
.btn{position:absolute;display:flex;align-items:center;justify-content:center;font-family:'Quicksand',sans-serif;font-weight:700;font-size:15px;text-transform:uppercase}
.btn-solid{background:var(--purple);color:var(--white)}
.btn-outline{border:2px solid var(--purple);color:var(--purple)}
.dots span{position:absolute;top:580px;width:12px;height:12px;border-radius:50%;background:var(--white)}
.dots span.active{background:var(--purple)}

/* pill tabs */
.pill{position:absolute;height:43px;border:1.5px solid var(--purple);border-radius:22px;display:flex;align-items:center;justify-content:center;font-size:13px;color:#333;background:var(--white)}
.pill.active{background:var(--purple);color:var(--white)}

/* intro */
.intro-photo{position:absolute;left:112px;top:944px;width:408px;height:320px;border-radius:26px;background:linear-gradient(135deg,#e9e9ec,#b9bcc3 60%,#5c5f66);box-shadow:0 6px 18px rgba(0,0,0,.15)}
.intro-frame{position:absolute;left:126px;top:950px;width:394px;height:314px;border:2px solid var(--purple);border-radius:26px}
.intro-title{left:596px;top:988px;font-size:29px;font-weight:600}
.intro-text{left:599px;top:1057px;width:489px;font-size:14px;line-height:26px;text-align:justify}

/* about */
.about{position:absolute;left:0;top:1353px;width:1200px;height:601px;background:var(--grey)}
.about-band{position:absolute;left:0;top:0;width:937px;height:601px;background:linear-gradient(90deg,#5b2a9a,#5a2d95)}
.about-title{left:111px;top:80px;font-size:30px;font-weight:600;color:var(--white)}
.about-text{left:111px;top:137px;width:487px;font-size:14.5px;line-height:25px;color:var(--white);text-align:justify}
.about-btn{left:111px;top:471px;width:145px;height:45px;background:var(--white);color:var(--purple);font-family:'Lato',sans-serif;font-size:14px}
.about-photo{position:absolute;left:708px;top:102px;width:381px;height:395px;background:linear-gradient(135deg,#d8d2c8,#8a7e72 55%,#3e3a38)}

/* services */
.section-title{position:absolute;left:0;width:1200px;text-align:center;font-family:'Quicksand',sans-serif;font-weight:600;font-size:29px;color:var(--ink)}
.service-card{position:absolute;top:2113px;width:305px;height:412px;background:var(--white);border-radius:14px;box-shadow:0 2px 12px rgba(0,0,0,.14);text-align:center}
.service-icon{position:absolute;left:80px;top:34px;width:146px;height:146px;border-radius:50%;background:var(--white);box-shadow:0 2px 10px rgba(0,0,0,.14);display:flex;align-items:center;justify-content:center}
.service-name{position:absolute;top:214px;width:100%;font-family:'Quicksand',sans-serif;font-weight:700;font-size:21px;color:var(--ink)}
.service-text{position:absolute;top:260px;left:30px;width:245px;font-size:14px;line-height:26px}
.service-more{position:absolute;top:362px;width:100%;font-family:'Quicksand',sans-serif;font-weight:700;font-size:14px;color:var(--purple)}
.slider-arrow{position:absolute;top:2303px;width:36px;height:36px;border:1.5px solid var(--purple);border-radius:50%}

/* register */
.register{position:absolute;left:0;top:2612px;width:1200px;height:921px;background:linear-gradient(180deg,#ddd6e8,#e7e2ee 50%,#d9d2e4)}
.register-title{top:173px}
.register-sub{position:absolute;left:0;width:1200px;top:214px;text-align:center;font-size:14.5px;color:#222}
.field{position:absolute;height:63px;background:var(--white);border-radius:3px;box-shadow:0 1px 4px rgba(0,0,0,.08);font-size:14px;color:#555;display:flex;align-items:center;padding-left:22px}
.field svg{position:absolute;right:22px;top:27px}
.submit{left:535px;top:800px;width:128px;height:52px;font-family:'Lato',sans-serif;font-weight:700}

/* team */
.member{position:absolute;top:3686px;width:232px;text-align:center}
.member-photo{width:232px;height:228px;border:2px solid var(--purple);padding:5px;background:var(--white)}
.member-photo div{width:100%;height:100%;background:linear-gradient(180deg,#d6d6d6,#8c8c8c)}
.member-name{margin-top:14px;font-family:'Quicksand',sans-serif;font-weight:700;font-size:19px;color:var(--ink)}
.member-link{margin:12px auto 0;width:14px;height:14px;background:var(--purple);border-radius:2px}
.member-role{margin-top:10px;font-size:14px;color:#333}

/* footer */
.site-footer{position:absolute;left:0;top:4101px;width:1200px;height:360px;background:var(--footer);color:var(--white)}
.footer-brand{left:112px;top:88px;font-family:'Quicksand',sans-serif;font-weight:700;font-size:44px}
.social span{position:absolute;top:184px;width:36px;height:36px;border-radius:50%;background:var(--white)}
.social span:first-child{background:var(--purple)}
.footer-divider{position:absolute;left:392px;top:70px;width:1px;height:180px;background:#2a2a2a}
.footer-col h4{position:absolute;top:68px;font-family:'Quicksand',sans-serif;font-weight:700;font-size:19px}
.footer-col a,.footer-col p{position:absolute;font-size:14px;color:var(--white);text-decoration:none;display:flex;align-items:center;gap:9px}
.copyright{position:absolute;left:0;width:1200px;top:306px;text-align:center;font-size:14px}
</style>
</head>
<body>

<header class="site-header">
  <nav class="main-nav">
    <a style="left:480px">Kund</a>
    <a style="left:566px">Konsulter &amp; Partners</a>
    <a style="left:790px">Om Tarnholm</a>
    <a style="left:916px">Kontakt</a>
  </nav>
  <svg class="search-icon" width="20" height="20" viewBox="0 0 20 20"><circle cx="8" cy="8" r="6" fill="none" stroke="#5b2a9a" stroke-width="2.6"/><line x1="12.5" y1="12.5" x2="18" y2="18" stroke="#5b2a9a" stroke-width="2.8" stroke-linecap="round"/></svg>
</header>
<div class="brand-box"><span class="brand-name">TARNHOLM</span></div>

<section class="hero" role="img" aria-label="Stadsvy över vattnet i solnedgång">
  <h1 class="hero-title">VI HJÄLPER DITT FÖRETAG<br>ATT VÄXA</h1>
  <a class="btn btn-solid" style="left:459px;top:294px;width:128px;height:54px">Uppgifter</a>
  <a class="btn btn-outline" style="left:613px;top:294px;width:128px;height:54px">Konsulter</a>
  <div class="dots"><span style="left:562px"></span><span class="active" style="left:583px"></span><span style="left:604px"></span><span style="left:625px"></span></div>
</section>

<div class="pill active" style="left:118px;top:849px;width:199px">Söker du spetskompetens?</div>
<div class="pill" style="left:327px;top:849px;width:163px">Tarnholm har lösningen</div>
<div class="pill" style="left:502px;top:849px;width:277px">Ett axplock av våra kompetensområden</div>
<div class="pill" style="left:793px;top:849px;width:120px">Kundreferens</div>
<div class="pill" style="left:928px;top:849px;width:155px">Söker ni kompetens?</div>

<div class="intro-frame"></div>
<div class="intro-photo" role="img" aria-label="Två personer skakar hand vid ett skrivbord"></div>
<h2 class="abs heading intro-title">Söker du spetskompetens?</h2>
<p class="abs intro-text">Vi erbjuder ett komplett konsultmäkleri med personliga, enkla och etablerade processer som gör att vi snabbt kan hjälpa er med inköp av specialistkompetens. Tillsammans med vårt nätverk och vår anpassningsbara organisation kan vi leverera inom Ekonomi, HR och IT. Våra kunder finns över hela Sverige såväl inom den privata som det offentliga sektorn.</p>

<section class="about">
  <div class="about-band"></div>
  <svg class="abs" style="left:648px;top:66px" width="170" height="220"><g fill="#9b86c2">
    <circle cx="3" cy="3" r="2"/><circle cx="42" cy="3" r="2"/><circle cx="81" cy="3" r="2"/><circle cx="120" cy="3" r="2"/><circle cx="159" cy="3" r="2"/>
    <circle cx="3" cy="42" r="2"/><circle cx="3" cy="81" r="2"/><circle cx="3" cy="120" r="2"/><circle cx="3" cy="159" r="2"/><circle cx="3" cy="198" r="2"/></g></svg>
  <h2 class="abs heading about-title">Om Tarnholm</h2>
  <p class="abs about-text">Tarnholm är en del av Varnex vars fokus ligger på bemanning och rekrytering medan vi på Tarnholm fokuserar på konsultmäklartjänster. Vi arbetar professionellt och personligt och har bred erfarenhet av Ekonomi, HR och IT. Vårt driv är att förstärka och komplettera våra kunders organisationer med specialistkunskap inom just dessa områden med bland annat systemutveckling, projektledning, redovisning, ekonomistyrning och verksamhetsutveckling. Med hjälp av våra väletablerade nätverk av underleverantörer/partners kan vi skräddarsy processen efter behov och förenkla inköpen av kvalificerad kompetens. Namnet Tarnholm står för "problemlösare, problemfri". Vår ambition är att vi ska göra just det för våra kunder; underlätta, lösa problem och minska friktionen i den löpande verksamheten.</p>
  <a class="btn about-btn">Lär dig mer</a>
  <div class="about-photo" role="img" aria-label="Kollegor i möte tittar på dokument"></div>
</section>

<h2 class="section-title" style="top:2032px">MSP</h2>
<div class="slider-arrow" style="left:55px"><svg width="34" height="34"><path d="M19 11 L13 17 L19 23" fill="none" stroke="#5b2a9a" stroke-width="2"/></svg></div>
<div class="slider-arrow" style="left:1108px;border-color:#888"><svg width="34" height="34"><path d="M15 11 L21 17 L15 23" fill="none" stroke="#666" stroke-width="1.6"/></svg></div>

<article class="service-card" style="left:114px">
  <div class="service-icon"><svg width="60" height="60" viewBox="0 0 60 60" fill="none" stroke="#5b2a9a" stroke-width="2"><rect x="12" y="8" width="32" height="42" rx="2"/><line x1="20" y1="30" x2="38" y2="30"/><line x1="20" y1="37" x2="38" y2="37"/><circle cx="22" cy="18" r="6"/><path d="M34 46 L50 30"/></svg></div>
  <h3 class="service-name">Avtalshantering</h3>
  <p class="service-text">Lorem ipsum dolor sit amet, consectetur adipiscing elit, seddo eiusmod tempor incididunt</p>
  <a class="service-more">Läs mer</a>
</article>
<article class="service-card" style="left:449px">
  <div class="service-icon"><svg width="60" height="60" viewBox="0 0 60 60" fill="none" stroke="#5b2a9a" stroke-width="2"><rect x="12" y="14" width="28" height="38" rx="2"/><line x1="18" y1="26" x2="34" y2="26"/><line x1="18" y1="33" x2="34" y2="33"/><line x1="18" y1="40" x2="30" y2="40"/><circle cx="42" cy="16" r="9"/></svg></div>
  <h3 class="service-name">Fakturering</h3>
  <p class="service-text">Lorem ipsum dolor sit amet, consectetur adipiscing elit, seddo eiusmod tempor incididunt</p>
  <a class="service-more">Läs mer</a>
</article>
<article class="service-card" style="left:783px">
  <div class="service-icon"><svg width="60" height="60" viewBox="0 0 60 60" fill="none" stroke="#5b2a9a" stroke-width="2"><rect x="10" y="36" width="7" height="14"/><rect x="21" y="30" width="7" height="20"/><rect x="32" y="34" width="7" height="16"/><rect x="43" y="24" width="7" height="26"/><polyline points="12,26 24,18 35,24 48,12"/><line x1="6" y1="50" x2="54" y2="50"/></svg></div>
  <h3 class="service-name">Statistik</h3>
  <p class="service-text">Lorem ipsum dolor sit amet, consectetur adipiscing elit, seddo eiusmod tempor incididunt</p>
  <a class="service-more">Läs mer</a>
</article>

<section class="register" aria-label="Registrera profil">
  <div class="pill" style="left:151px;top:71px;width:161px;background:transparent">Konsulter &amp; partners</div>
  <div class="pill" style="left:331px;top:71px;width:163px;background:transparent">Varför välja Tarnholm?</div>
  <div class="pill" style="left:516px;top:71px;width:184px;background:transparent">Urval av våra ramavtal</div>
  <div class="pill" style="left:720px;top:71px;width:146px;background:transparent">Aktuella uppdrag</div>
  <div class="pill active" style="left:897px;top:71px;width:153px">Registrera profil</div>
  <h2 class="section-title register-title">Registrera profil</h2>
  <p class="register-sub">Låter det intressant? Fyll i formuläret nedan så kontaktar vi dig när vi hittar en lämplig tjänst.</p>
  <div class="field" style="left:204px;top:279px;width:383px">Namn</div>
  <div class="field" style="left:611px;top:279px;width:385px">Företag</div>
  <div class="field" style="left:204px;top:362px;width:792px">E-post</div>
  <div class="field" style="left:204px;top:448px;width:383px">Telefonnummer</div>
  <div class="field" style="left:611px;top:448px;width:385px">Ort</div>
  <div class="field" style="left:204px;top:533px;width:792px">Expertområde<svg width="10" height="6"><path d="M0 0 L5 5 L10 0" fill="none" stroke="#888"/></svg></div>
  <div class="field" style="left:204px;top:620px;width:383px">Tillgänglighet</div>
  <div class="field" style="left:611px;top:620px;width:385px">Omfattning</div>
  <div class="field" style="left:204px;top:706px;width:792px">Välj Cv Att Ladda Upp<svg width="10" height="6"><path d="M0 0 L5 5 L10 0" fill="none" stroke="#888"/></svg></div>
  <a class="btn btn-solid submit">Skicka</a>
</section>

<h2 class="section-title" style="top:3617px">Vi på Tarnholm</h2>
<div class="member" style="left:177px">
  <div class="member-photo"><div role="img" aria-label="Porträttfoto av Elin Sandberg"></div></div>
  <p class="member-name">Elin Sandberg</p><div class="member-link"></div>
  <p class="member-role">Leverans- och partneransvarig</p>
</div>
<div class="member" style="left:483px">
  <div class="member-photo"><div role="img" aria-label="Porträttfoto av Sara Lindqvist"></div></div>
  <p class="member-name">Sara Lindqvist</p><div class="member-link"></div>
  <p class="member-role">Leverans- och partneransvarig</p>
</div>
<div class="member" style="left:790px">
  <div class="member-photo"><div role="img" aria-label="Porträttfoto av Maja Ekström"></div></div>
  <p class="member-name">Maja Ekström</p><div class="member-link"></div>
  <p class="member-role">Leveranskoordinator</p>
</div>

<footer class="site-footer">
  <div class="abs footer-brand">TARNHOLM</div>
  <div class="social" aria-label="Sociala medier"><span style="left:112px"></span><span style="left:155px"></span><span style="left:197px"></span><span style="left:240px"></span></div>
  <div class="footer-divider"></div>
  <div class="footer-col">
    <h4 style="left:431px">Snabblänkar</h4>
    <a style="left:431px;top:108px">»&nbsp; Kund</a>
    <a style="left:431px;top:134px">»&nbsp; Konsulter &amp; Partners</a>
    <a style="left:431px;top:160px">»&nbsp; Om Tarnholm</a>
    <a style="left:431px;top:186px">»&nbsp; Kontakt</a>
  </div>
  <div class="footer-col">
    <h4 style="left:639px">Vårt företag</h4>
    <a style="left:639px;top:108px">»&nbsp; Allmänna Villkor</a>
    <a style="left:639px;top:134px">»&nbsp; Integritetspolicy</a>
    <a style="left:639px;top:160px">»&nbsp; Om oss</a>
    <a style="left:639px;top:186px">»&nbsp; Stöd</a>
  </div>
  <div class="footer-col">
    <h4 style="left:864px">Kontakta oss</h4>
    <p style="left:864px;top:108px;align-items:flex-start"><svg width="12" height="16" viewBox="0 0 12 16"><path d="M6 0 C2.7 0 0 2.6 0 5.8 C0 10 6 16 6 16 C6 16 12 10 12 5.8 C12 2.6 9.3 0 6 0Z" fill="#fff"/><circle cx="6" cy="6" r="2.2" fill="#0c0c0c"/></svg><span>Granitvägen 22 116 45<br>Stockholm</span></p>
    <p style="left:864px;top:177px"><svg width="14" height="14" viewBox="0 0 14 14"><path d="M3 0 L5.5 3.5 L4 5.5 C5 7.5 6.5 9 8.5 10 L10.5 8.5 L14 11 L12 14 C6 13.5 0.5 8 0 2Z" fill="#fff"/></svg>+46 (0) 8-555 012 34</p>
    <p style="left:864px;top:218px"><svg width="16" height="12" viewBox="0 0 16 12"><rect width="16" height="12" rx="1" fill="#fff"/><path d="M0 1 L8 7 L16 1" fill="none" stroke="#0c0c0c" stroke-width="1.4"/></svg>info@tarnholm.se</p>
  </div>
  <p class="copyright">©Copyrights 2022 Tarnholm | Alla rättigheter förbehållna</p>
</footer>

</body>
</html>
```